A business selling natural soaps online and in farmers markets. I want it to reflect local commerce and natural lifestyle. My colors are olive green and saddle brown. I want the dimensions to be 2.25 x 3.25" with matte finish.
Updates

The name of my company is Fern Hollow Soapworks, LLC

Industry/Entity Type

Business

```html
<!DOCTYPE html>
<html lang="en">
<head>
<meta charset="utf-8">
<title>Fern Hollow Soapworks, LLC – Business Card</title>
<link href="https://fonts.googleapis.com/css2?family=Courgette&family=Gelasio:wght@400&display=swap" rel="stylesheet">
<style>
  :root {
    --page-bg: #efebe4;
    --card-frame: #bfa36c;
    --card-face: #ffffff;
    --olive: #6f6114;
    --ornament-light: #d9c7a3;
    --ornament-deep: #8a7a3a;
  }
  * { box-sizing: border-box; margin: 0; padding: 0; }
  html, body {
    width: 1200px;
    height: 1000px;
    overflow: hidden;
    background: var(--page-bg);
  }
  .canvas {
    width: 1200px;
    height: 1000px;
    display: flex;
    align-items: center;
    justify-content: center;
  }
  .business-card {
    width: 1000px;
    height: 600px;
    background: var(--card-frame);
    padding: 30px;
    box-shadow: 0 6px 18px rgba(0,0,0,0.12);
  }
  .card-face {
    position: relative;
    width: 100%;
    height: 100%;
    background: var(--card-face);
    display: flex;
    flex-direction: column;
    align-items: center;
  }
  .brand-mark {
    margin-top: 70px;
    width: 110px;
    height: 110px;
    border-radius: 50%;
    background: var(--olive);
  }
  .brand-name {
    margin-top: 40px;
    font-family: "Courgette", cursive;
    font-size: 44px;
    color: var(--olive);
    letter-spacing: 1px;
  }
  .flourish {
    margin-top: 30px;
    width: 250px;
    height: 50px;
    border-radius: 25px;
    background: linear-gradient(90deg, var(--ornament-light), var(--ornament-deep), var(--ornament-light));
    opacity: 0.55;
  }
  .contact-line {
    position: absolute;
    left: 0;
    right: 0;
    bottom: 70px;
    display: flex;
    justify-content: center;
    gap: 34px;
    font-family: "Gelasio", Georgia, serif;
    font-size: 27px;
    color: var(--olive);
    letter-spacing: 0.5px;
  }
</style>
</head>
<body>
  <main class="canvas">
    <section class="business-card">
      <div class="card-face">
        <div class="brand-mark" aria-hidden="true"></div>
        <h1 class="brand-name">Fern Hollow Soapworks, LLC</h1>
        <div class="flourish" role="img" aria-label="Decorative scrolled flourish ornament"></div>
        <p class="contact-line">
          <span class="contact-phone">08512360.794</span>
          <span class="contact-email">info@fernhollowsoap.com</span>
          <span class="contact-address">Linden Falls, Virginia 22190</span>
        </p>
      </div>
    </section>
  </main>
</body>
</html>
```